Explosive, chemical reaction of creativity!

Web design for a digital marketing company. The unconventional is encouraged!
This is for a cool, young, geographically diverse company (artmingle... you are all part of our team!!!)... we build websites but our real specialty is "search experience optimization".... creating conversion focused content, SEO (including content), and social media.

Target Market(s)

small to medium size businesses, law firms, medical practices, municipalities

Industry/Entity Type

Marketing

Number of Pages Required

2 page

Requirements
Must have
• WOW
• something different and special... we've been playing with a science theme (www.vexmorrow.marketing) but we are open to different looks, layouts, etc.
• we nee a homepage design and an interior page design
• content needs to include: Marketing Catalysts (about us), Our Formula (services), Chemical Reactions(Results/Our Clients),
• FREE Web Prism Audit
• Let us put together an objective snapshot of your digital presence for you.
Nice to have
• we are open to the use of background video (chemical reaction???)
• we are open to cool and different imagery
Should not have
• template look like most other websites

```html
<!DOCTYPE html>
<html lang="en">
<head>
<meta charset="utf-8">
<title>Vexmorrow Digital Marketing</title>
<link href="https://fonts.googleapis.com/css2?family=Open+Sans:wght@400;600;700;800&display=swap" rel="stylesheet">
<style>
:root{
  --blue:#1b8fd9;
  --blue-dark:#12609e;
  --ink:#333a40;
  --muted:#6d747a;
  --band:#080a10;
  --panel:#ececec;
  --footer:#1d1f22;
  --footer-text:#9aa0a6;
  --white:#ffffff;
}
*{box-sizing:border-box;margin:0;padding:0}
html,body{width:1200px;height:2276px;overflow:hidden}
body{font-family:"Open Sans",Arial,sans-serif;color:var(--ink);background:var(--white);position:relative}
.wrap{width:1040px;margin:0 auto;position:relative}
h2.section-title{font-size:30px;font-weight:700;color:var(--blue-dark);line-height:1.25}
.section-sub{font-size:13px;color:var(--muted);margin-top:2px}

/* hero */
.hero{position:relative;height:440px;background:linear-gradient(100deg,#dfe6ec 0%,#c8d2da 45%,#e9edf0 100%)}
.hero-photo{position:absolute;inset:0}
.brand{position:absolute;left:48px;top:14px;display:flex;align-items:center;gap:10px}
.brand-mark{width:30px;height:30px;background:var(--blue);border-radius:50%}
.brand-name{font-size:17px;font-weight:700;color:var(--blue-dark);letter-spacing:.5px;line-height:1.05;text-transform:uppercase;width:160px}
.menu-btn{position:absolute;right:22px;top:16px;width:26px}
.menu-btn span{display:block;height:3px;background:#222;margin-bottom:5px}
.hero-box{position:absolute;left:260px;top:176px;width:290px;padding:16px 18px;background:rgba(20,40,70,.55);color:var(--white)}
.hero-box h1{font-size:22px;font-weight:700;line-height:1.25}
.hero-box p{font-size:11px;line-height:1.5;margin-top:8px;color:#dfe9f2}

/* data */
.data{height:280px;padding-top:22px}
.data-grid{display:grid;grid-template-columns:1fr 1fr;gap:14px 26px;margin-top:16px}
.data-card{background:var(--panel);padding:14px 18px;font-size:11px;line-height:1.55;color:var(--muted);height:78px}

/* stats */
.stats{height:180px;background:var(--band);display:flex;align-items:center}
.stats .wrap{display:flex;justify-content:space-between}
.stat{display:flex;align-items:center;gap:10px;width:190px}
.ring{position:relative;width:76px;height:76px;flex:none}
.ring svg{position:absolute;inset:0}
.ring b{position:absolute;inset:0;display:flex;align-items:center;justify-content:center;color:var(--white);font-size:18px}
.stat p{color:#c9ced3;font-size:10.5px;line-height:1.45}

/* formula */
.formula{height:250px;padding-top:22px}
.formula-grid{display:grid;grid-template-columns:repeat(3,1fr);gap:40px;margin-top:18px;text-align:center}
.formula-item svg{height:48px}
.formula-item h3{font-size:20px;color:var(--blue-dark);margin:6px 0}
.formula-item p{font-size:11px;line-height:1.55;color:var(--muted)}

/* facts */
.facts-head{height:72px;padding-top:10px}
.facts{height:125px;background:var(--band);display:flex;align-items:center}
.facts .wrap{display:flex;justify-content:space-around}
.fact{display:flex;align-items:center;gap:12px}
.fact-num{width:64px;height:64px;border-radius:50%;background:var(--blue);color:var(--white);font-weight:700;font-size:20px;display:flex;align-items:center;justify-content:center}
.fact p{color:#c9ced3;font-size:11px;line-height:1.4;width:120px}

/* clients */
.clients{height:145px;padding-top:14px}
.testimonials{display:grid;grid-template-columns:1fr 1fr;gap:40px;margin-top:12px}
.testimonial{display:flex;gap:14px}
.avatar{width:62px;height:70px;flex:none;background:linear-gradient(#b9c3cc,#7d8893)}
.testimonial h4{font-size:12px;color:var(--blue-dark)}
.testimonial p{font-size:10.5px;line-height:1.5;color:var(--muted);margin-top:3px}

/* partners */
.partners{height:90px;background:#e7e8ea;display:flex;align-items:center}
.partners .wrap{display:flex;justify-content:center;gap:22px;align-items:center}
.partner{width:150px;height:58px;background:var(--white);display:flex;align-items:center;justify-content:center;font-weight:700;font-size:17px;color:#44505c}
.arrow{color:#555;font-size:22px}

/* blog */
.blog{height:395px;padding-top:20px}
.blog-grid{display:grid;grid-template-columns:repeat(3,1fr);gap:24px;margin-top:14px}
.post{background:#eef0f2;text-align:center;padding-bottom:14px}
.post-img{height:130px;position:relative}
.post-date{position:absolute;left:10px;bottom:-14px;width:42px;height:42px;background:var(--blue);color:var(--white);font-size:10px;font-weight:700;display:flex;align-items:center;justify-content:center;line-height:1.1;text-align:center}
.post h3{font-size:15px;color:var(--ink);margin:22px 14px 8px}
.post p{font-size:10.5px;color:var(--muted);line-height:1.5;padding:0 16px}
.btn{display:inline-block;margin-top:12px;background:var(--blue-dark);color:var(--white);font-size:11px;padding:6px 20px}
.blog-nav{text-align:center;margin-top:14px;color:#555;font-size:16px}

/* footer */
.footer{height:269px;background:var(--footer);padding-top:28px;color:var(--footer-text)}
.footer-grid{display:grid;grid-template-columns:1fr 1.3fr 1fr;gap:40px;font-size:11px}
.footer h5{color:var(--white);font-size:12px;margin-bottom:10px;letter-spacing:.5px}
.footer li{list-style:none;line-height:1.9}
.field{background:#2c2f33;height:20px;margin-bottom:8px}
.field.area{height:46px}
.send{background:var(--blue);color:var(--white);width:90px;text-align:center;padding:4px;margin:0 auto}
.socials{display:flex;gap:10px;justify-content:center;margin-top:14px}
.socials span{width:24px;height:24px;border-radius:50%;background:var(--blue)}
.contact li{display:flex;gap:8px;align-items:center}
.dot{width:8px;height:8px;border-radius:50%;background:var(--blue);flex:none}
.bottom-bar{position:absolute;left:0;right:0;bottom:0;height:32px;background:var(--blue-dark);color:#d7e6f3;font-size:10px}
.bottom-bar .wrap{display:flex;justify-content:space-between;line-height:32px}
</style>
</head>
<body>

<header class="hero">
  <div class="hero-photo" role="img" aria-label="Office scene with a smiling businessman in a suit at a laptop"></div>
  <div class="brand"><span class="brand-mark"></span><span class="brand-name">Vexmorrow Digital Marketing</span></div>
  <div class="menu-btn"><span></span><span></span><span></span></div>
  <div class="hero-box">
    <h1>Porta quam semper in Vexmorrow science</h1>
    <p>Search experience optimization that mixes content, SEO and social into one reaction.</p>
  </div>
</header>

<section class="data">
  <div class="wrap">
    <h2 class="section-title">Using Data for Success</h2>
    <p class="section-sub">Every campaign starts with real numbers, clear goals and a plan to measure them.</p>
    <div class="data-grid">
      <div class="data-card">We study how your visitors search, click and convert, then shape every page around that path. Small changes in structure and copy often lead to large gains in leads and calls.</div>
      <div class="data-card">Our reports show what works and what does not, in plain language. You see traffic, rankings and conversions side by side so decisions become simple and fast.</div>
      <div class="data-card">We test headlines, layouts and offers against each other. The winning version stays, the rest is dropped, and your site keeps improving month after month.</div>
      <div class="data-card">From local law firms to city services, we tune content for the people you serve. Ask for a free Web Prism Audit and get an honest snapshot of your digital presence.</div>
    </div>
  </div>
</section>

<section class="stats">
  <div class="wrap">
    <div class="stat"><div class="ring"><svg viewBox="0 0 76 76"><circle cx="38" cy="38" r="33" fill="none" stroke="#2a2f38" stroke-width="5"/><circle cx="38" cy="38" r="33" fill="none" stroke="#1b8fd9" stroke-width="5" stroke-dasharray="193 207" transform="rotate(-90 38 38)"/></svg><b>93%</b></div><p>of online journeys begin with a search engine</p></div>
    <div class="stat"><div class="ring"><svg viewBox="0 0 76 76"><circle cx="38" cy="38" r="33" fill="none" stroke="#2a2f38" stroke-width="5"/><circle cx="38" cy="38" r="33" fill="none" stroke="#1b8fd9" stroke-width="5" stroke-dasharray="145 207" transform="rotate(-90 38 38)"/></svg><b>70%</b></div><p>of clicks go to organic search results</p></div>
    <div class="stat"><div class="ring"><svg viewBox="0 0 76 76"><circle cx="38" cy="38" r="33" fill="none" stroke="#2a2f38" stroke-width="5"/><circle cx="38" cy="38" r="33" fill="none" stroke="#1b8fd9" stroke-width="5" stroke-dasharray="170 207" transform="rotate(-90 38 38)"/></svg><b>82%</b></div><p>of buyers research a business online first</p></div>
    <div class="stat"><div class="ring"><svg viewBox="0 0 76 76"><circle cx="38" cy="38" r="33" fill="none" stroke="#2a2f38" stroke-width="5"/><circle cx="38" cy="38" r="33" fill="none" stroke="#1b8fd9" stroke-width="5" stroke-dasharray="145 207" transform="rotate(-90 38 38)"/></svg><b>70%</b></div><p>of links users click on are organic</p></div>
    <div class="stat"><div class="ring"><svg viewBox="0 0 76 76"><circle cx="38" cy="38" r="33" fill="none" stroke="#2a2f38" stroke-width="5"/><circle cx="38" cy="38" r="33" fill="none" stroke="#1b8fd9" stroke-width="5" stroke-dasharray="103 207" transform="rotate(-90 38 38)"/></svg><b>50%</b></div><p>of searches now come from mobile devices</p></div>
  </div>
</section>

<section class="formula">
  <div class="wrap">
    <h2 class="section-title">The Perfect Digital Marketing Formula!</h2>
    <p class="section-sub">Three elements that react together to grow your business.</p>
    <div class="formula-grid">
      <div class="formula-item">
        <svg viewBox="0 0 60 48"><rect x="4" y="4" width="52" height="32" rx="2" fill="none" stroke="#1b8fd9" stroke-width="4"/><rect x="24" y="36" width="12" height="6" fill="#1b8fd9"/><rect x="16" y="42" width="28" height="4" fill="#1b8fd9"/></svg>
        <h3>Website</h3>
        <p>Fast, clean sites built to turn visitors into calls, forms and customers on every screen size.</p>
      </div>
      <div class="formula-item">
        <svg viewBox="0 0 40 48"><path d="M4 2h22l10 10v34H4z" fill="none" stroke="#1b8fd9" stroke-width="4"/><path d="M11 20h18M11 28h18M11 36h12" stroke="#1b8fd9" stroke-width="3"/></svg>
        <h3>Content</h3>
        <p>Conversion focused writing and SEO that answers real questions and earns lasting rankings.</p>
      </div>
      <div class="formula-item">
        <svg viewBox="0 0 48 48"><circle cx="36" cy="10" r="7" fill="#1b8fd9"/><circle cx="12" cy="24" r="7" fill="#1b8fd9"/><circle cx="36" cy="38" r="7" fill="#1b8fd9"/><path d="M36 10L12 24L36 38" fill="none" stroke="#1b8fd9" stroke-width="3"/></svg>
        <h3>Social</h3>
        <p>Social campaigns that spark talk, build trust and bring your audience back again and again.</p>
      </div>
    </div>
  </div>
</section>

<div class="facts-head"><div class="wrap"><h2 class="section-title">Some Facts About Our Catalysts</h2><p class="section-sub">Numbers from a busy team spread around the world.</p></div></div>
<section class="facts">
  <div class="wrap">
    <div class="fact"><div class="fact-num">35</div><p>Team members across many countries</p></div>
    <div class="fact"><div class="fact-num">10</div><p>Years of search and content work</p></div>
    <div class="fact"><div class="fact-num">234</div><p>Projects launched for our clients</p></div>
    <div class="fact"><div class="fact-num">1</div><p>Shared goal: your growth</p></div>
  </div>
</section>

<section class="clients">
  <div class="wrap">
    <h2 class="section-title">Our Client Says</h2>
    <div class="testimonials">
      <div class="testimonial"><div class="avatar" role="img" aria-label="Portrait photo of a client"></div><div><h4>Mara Lindqvist</h4><p>Our calls doubled within months. The team explained every step and the new site finally brings in the clients we want.</p></div></div>
      <div class="testimonial"><div class="avatar" role="img" aria-label="Portrait photo of a client"></div><div><h4>Dana Okafor</h4><p>Friendly, quick and creative. Our practice now ranks on page one and our social pages feel alive again.</p></div></div>
    </div>
  </div>
</section>

<section class="partners">
  <div class="wrap">
    <span class="arrow">‹</span>
    <div class="partner">Stallworth</div>
    <div class="partner">Kelvane</div>
    <div class="partner">Quantiva</div>
    <div class="partner">Tradeloom</div>
    <span class="arrow">›</span>
  </div>
</section>

<section class="blog">
  <div class="wrap">
    <h2 class="section-title">Our Blog</h2>
    <div class="blog-grid">
      <article class="post"><div class="post-img" role="img" aria-label="Photo of a businessman reading at his desk" style="background:linear-gradient(#c2cbd3,#6e7a86)"><span class="post-date">May<br>12</span></div><h3>Pro Receivers Will Now Be Optimized</h3><p>How small site changes can lift search traffic and help more of the right people find you.</p><span class="btn">Read More</span></article>
      <article class="post"><div class="post-img" role="img" aria-label="Photo of a speedometer showing next level" style="background:linear-gradient(#3a5f8a,#0d1f33)"><span class="post-date">May<br>18</span></div><h3>Take Your Business to the Next Level: 10 SEO Notes</h3><p>Ten simple steps to lift rankings, speed up pages and turn more clicks into leads.</p><span class="btn">Read More</span></article>
      <article class="post"><div class="post-img" role="img" aria-label="Photo of a hand touching a glowing digital screen" style="background:linear-gradient(#6fb3e6,#1d5c94)"><span class="post-date">May<br>24</span></div><h3>Start Early March Marketing Plans</h3><p>Plan your spring content now so campaigns are ready when your customers start searching.</p><span class="btn">Read More</span></article>
    </div>
    <div class="blog-nav">›</div>
  </div>
</section>

<footer class="footer">
  <div class="wrap footer-grid">
    <div><h5>SITE MAP</h5><ul><li>Home</li><li>Marketing Catalysts</li><li>Our Formula</li><li>Chemical Reactions</li><li>Blog</li><li>Contact</li></ul></div>
    <div><h5>SEND A MESSAGE</h5><div class="field"></div><div class="field"></div><div class="field area"></div><div class="send">Send Message</div><div class="socials"><span></span><span></span><span></span><span></span></div></div>
    <div><h5>GET IN TOUCH</h5><p>Ask for your free Web Prism Audit today.</p><ul class="contact"><li><span class="dot"></span>1480 Harbor Lane, Suite 9</li><li><span class="dot"></span>(555) 019-4471</li><li><span class="dot"></span>hello@vexmorrow.marketing</li><li><span class="dot"></span>www.vexmorrow.marketing</li></ul></div>
  </div>
  <div class="bottom-bar"><div class="wrap"><span>© Vexmorrow Digital Marketing. All rights reserved.</span><span>www.vexmorrow.marketing</span></div></div>
</footer>

</body>
</html>
```